Website design for KORVEL – data platform for healthcare & social housing

We’re looking for a clean, modern multi-page website design for KORVEL — a data platform for healthcare and social housing.

📎 Please read the attached PDF for full structure, context, and design guidance.
The briefing is essential to understanding this project.

➡️ For the initial submission, only the homepage design (including header and footer) is required.

This will help us assess design direction and fit.

The full project includes four levels (homepage, general page, product overview, and product detail), which will be completed after selecting the final designer.

Industry/Entity Type

data platform for healthcare & social housing

Number of Pages Required

1 page

Font styles to use
Sans Serif

Requirements
Must have
• Please read the attached PDF
Nice to have
Should not have

```html
<!DOCTYPE html>
<html lang="en">
<head>
<meta charset="utf-8">
<title>KORVEL – Data platform for healthcare and social housing</title>
<link rel="stylesheet" href="https://fonts.googleapis.com/css2?family=Poppins:wght@400;500;600&display=swap">
<style>
:root{
  --orange:#f47b20;
  --black:#000;
  --ink:#111;
  --muted:#555;
  --white:#fff;
  --navy:#0a0f1e;
  --deep-blue:#0b2a5a;
  --line:#2a2a2a;
}
*{box-sizing:border-box;margin:0;padding:0}
html,body{width:1200px;height:5173px;overflow:hidden}
body{font-family:"Poppins",sans-serif;color:var(--ink);background:var(--white);position:relative}
.section{position:absolute;left:0;width:1200px}
.btn{display:inline-block;font-size:13px;padding:8px 18px;border-radius:4px;border:1px solid var(--orange);color:var(--ink);background:transparent;font-weight:500}
.btn-fill{background:var(--orange);color:var(--white)}
.btn-light{background:var(--white);border-color:var(--white);color:var(--ink)}
.btn-ghost-light{border-color:var(--white);color:var(--white)}
.tag{display:inline-block;font-size:11px;padding:4px 12px;border-radius:3px;background:#eee;color:var(--ink)}
.tag-light{background:var(--white)}
.photo{border-radius:10px}

/* header */
.site-header{top:0;height:80px;display:flex;align-items:center;padding:0 56px}
.brand{font-weight:600;font-size:30px;letter-spacing:2px;color:var(--deep-blue)}
.nav{display:flex;gap:26px;margin-left:auto;margin-right:30px;font-size:13px}
.header-actions{display:flex;gap:10px}

/* hero */
.hero-banner{top:88px;left:56px;width:1088px;height:312px;border-radius:10px;background:linear-gradient(120deg,#0a1a3a,#1e6fd6 45%,#6fc2ff 55%,#0a2a66)}
.intro-card{top:412px;left:56px;width:444px;height:318px;background:var(--black);border-radius:10px;color:var(--white);padding:40px 36px;display:flex;flex-direction:column;justify-content:flex-end}
.intro-card h1{font-size:38px;font-weight:500;line-height:1.18}
.intro-card p{font-size:13px;margin:12px 0 18px;color:#ddd}
.intro-card .actions{display:flex;gap:10px}
.intro-photo{top:412px;left:512px;width:632px;height:318px;background:linear-gradient(135deg,#0c1c36,#2a5f9e 50%,#0d1e3a)}

/* about */
.about{top:800px;height:520px}
.about .tag{position:absolute;left:56px;top:30px}
.about h2{position:absolute;left:56px;top:62px;width:330px;font-size:36px;font-weight:500;line-height:1.25}
.about-photo{position:absolute;left:448px;top:54px;width:306px;height:426px;border-radius:18px;border:8px solid var(--orange);background:linear-gradient(160deg,#e8eef5,#9db3c8 60%,#4a6a8a)}
.about-text{position:absolute;left:790px;top:260px;width:350px;font-size:13px;line-height:1.6;color:var(--muted)}
.about .btn{position:absolute;left:790px;top:440px}

/* dark block */
.dark{top:1320px;height:1390px;background:var(--black);color:var(--white)}
.center-head{position:absolute;left:0;width:1200px;text-align:center}
.center-head h2{font-size:44px;font-weight:400;line-height:1.25;margin-top:14px}
.why{top:60px}
.tabs{position:absolute;left:56px;top:330px;width:376px}
.tab{display:flex;align-items:center;gap:12px;height:56px;padding:0 16px;font-size:14px;border-radius:6px}
.tab.active{background:var(--white);color:var(--ink)}
.tab .icon{width:22px;height:22px}
.tab .arrow{margin-left:auto}
.why-card{position:absolute;left:474px;top:236px;width:670px;height:310px;border-radius:10px;background:linear-gradient(150deg,#071530,#1b4f9a 55%,#081430);padding:34px}
.why-card h3{font-size:24px;font-weight:500}
.why-card p{font-size:13px;width:330px;margin:8px 0 16px;color:#dbe5f5;line-height:1.55}
.products-head{top:640px}
.products-head h2{width:760px;margin:14px auto 0}
.product-cards{position:absolute;top:880px;left:56px;display:flex;gap:32px}
.product-card{width:341px;height:346px;border:1px solid #444;border-radius:12px;overflow:hidden;display:flex;flex-direction:column;background:#060606}
.product-card .art{height:180px}
.product-card h3{font-size:20px;font-weight:500;text-align:center;margin-top:14px}
.product-card p{font-size:12px;text-align:center;color:#cfcfcf;padding:6px 30px;line-height:1.5}
.product-card .more{margin-top:auto;border-top:1px solid #444;height:52px;display:flex;align-items:center;justify-content:center;font-size:16px}

/* audience */
.audience{top:2760px;height:330px}
.audience .tag{position:absolute;left:56px;top:22px}
.audience h2{position:absolute;left:56px;top:56px;width:620px;font-size:40px;font-weight:500;line-height:1.2}
.audience p{position:absolute;left:56px;top:170px;width:600px;font-size:13px;color:var(--muted);line-height:1.6}
.audience .btn{position:absolute;left:56px;top:240px}
.audience-card{position:absolute;left:752px;top:8px;width:392px;height:290px;border-radius:10px;background:linear-gradient(140deg,#0d3c73,#3a74b6 55%,#0a2a55);color:var(--white);padding:20px 24px}
.audience-card .tag{position:static;background:var(--white)}
.audience-card h3{font-size:20px;font-weight:500;margin-top:12px;line-height:1.3}
.audience-card p{position:static;width:auto;color:#e2ecf8;margin:10px 0 14px;font-size:12px}
.audience-card .btn{position:static}

/* testimonial */
.testimonial{top:3100px;height:460px}
.testimonial .tag{position:absolute;left:56px;top:18px}
.testimonial h2{position:absolute;left:56px;top:58px;width:420px;font-size:40px;font-weight:500;line-height:1.25}
.quote-card{position:absolute;left:562px;top:20px;width:582px;height:400px;background:var(--orange);border-radius:6px;padding:36px 40px;color:var(--ink)}
.person{display:flex;align-items:center;gap:14px}
.avatar{width:58px;height:58px;border-radius:50%;background:linear-gradient(135deg,#f2c7a4,#b67a55);border:3px solid var(--white)}
.person strong{display:block;font-size:16px;font-weight:500}
.person span{font-size:11px}
.quote-card blockquote{font-size:20px;font-weight:500;line-height:1.45;margin:26px 0 26px;color:var(--white)}
.pager{display:flex;gap:14px;font-size:13px;align-items:center}
.quote-card .btn{margin-top:24px;border-color:var(--ink);background:var(--white)}

/* partners */
.partners{top:3600px;height:80px;display:flex;align-items:center;justify-content:space-between;padding:0 20px}
.partner{width:110px;height:26px;border-radius:4px;background:#e4e4e4}

/* action */
.action{top:3720px;height:180px}
.action h2{position:absolute;left:56px;top:10px;font-size:40px;font-weight:500}
.action p{position:absolute;left:56px;top:72px;width:520px;font-size:13px;color:var(--muted);line-height:1.6}
.action .buttons{position:absolute;right:56px;top:84px;display:flex;gap:10px}

/* community */
.community{top:3900px;height:350px;background:linear-gradient(90deg,#0d0d0d,#2d2a26 60%,#5a4a3c);color:var(--white)}
.community .tag{position:absolute;left:56px;top:20px;background:var(--white)}
.community h2{position:absolute;left:56px;top:56px;width:600px;font-size:40px;font-weight:500;line-height:1.2}
.community p{position:absolute;left:56px;top:170px;width:460px;font-size:13px;line-height:1.6;color:#ddd}
.community .buttons{position:absolute;left:56px;top:244px;display:flex;gap:10px}

/* contact */
.contact{top:4250px;height:540px}
.contact h2{position:absolute;left:56px;top:42px;width:420px;font-size:40px;font-weight:500;line-height:1.2}
.form{position:absolute;left:56px;top:270px;width:580px}
.row{display:flex;gap:40px;margin-bottom:26px}
.field{flex:1;font-size:13px;border-bottom:1px solid #999;padding-bottom:8px}
.form .btn{margin-top:4px}
.contact-photo{position:absolute;left:734px;top:30px;width:410px;height:432px;border-radius:6px;background:linear-gradient(160deg,#071a3a,#1e63b8 55%,#0a1a33);color:var(--white);padding:22px 26px;font-size:14px;line-height:1.5}

/* footer */
.site-footer{top:4790px;height:383px;background:var(--navy);color:var(--white)}
.footer-brand{position:absolute;left:56px;top:50px;font-size:40px;font-weight:600;letter-spacing:3px;color:var(--white)}
.socials{position:absolute;left:56px;top:126px;display:flex;gap:14px}
.socials span{width:26px;height:26px;border-radius:50%;background:#1f3a8a}
.col{position:absolute;top:50px;font-size:13px;line-height:2}
.col h4{color:var(--orange);font-size:15px;font-weight:500;margin-bottom:4px}
.bottom{position:absolute;left:56px;right:56px;top:330px;border-top:1px solid #2a3350;padding-top:14px;font-size:12px;display:flex;color:#cfd5e6}
.bottom .links{margin-left:auto;display:flex;gap:24px}
</style>
</head>
<body>

<header class="section site-header">
  <div class="brand">KORVEL</div>
  <nav class="nav"><span>What is KORVEL?</span><span>Products</span><span>Who it's for</span><span>Community</span><span>About us</span><span>Contact us</span></nav>
  <div class="header-actions"><span class="btn">Start KORVEL</span><span class="btn btn-fill">Plan a demo</span></div>
</header>

<div class="section hero-banner" role="img" aria-label="Abstract blue data streams"></div>

<section class="section intro-card">
  <h1>More impact with better control over data</h1>
  <p>Data analytics for healthcare and social housing</p>
  <div class="actions"><span class="btn btn-light">Products</span><span class="btn">Plan a demo</span></div>
</section>
<div class="section intro-photo photo" role="img" aria-label="Hands working on a laptop with data dashboards"></div>

<section class="section about">
  <span class="tag">About KORVEL</span>
  <h2>Revolutionizing Data Use in Healthcare and Social Housing</h2>
  <div class="about-photo" role="img" aria-label="Professional holding a tablet in an office"></div>
  <p class="about-text">KORVEL is a data analytics platform for the healthcare sector and social housing sector. It helps organizations unlock, analyze, and use data to make smarter decisions. KORVEL combines accessible platform with intelligent tools, a professional community, and BI-as-a-Service.</p>
  <span class="btn btn-fill">Read more</span>
</section>

<section class="section dark">
  <div class="center-head why">
    <span class="tag tag-light">Why KORVEL Works</span>
    <h2>KORVEL turns disconnected data into<br>powerful decisions.</h2>
  </div>
  <div class="tabs">
    <div class="tab active">
      <svg class="icon" viewBox="0 0 24 24"><circle cx="12" cy="8" r="3" fill="none" stroke="#111" stroke-width="1.6"/><path d="M5 19c1-4 13-4 14 0" fill="none" stroke="#111" stroke-width="1.6"/></svg>
      Community<span class="arrow">›</span></div>
    <div class="tab">
      <svg class="icon" viewBox="0 0 24 24"><rect x="4" y="4" width="16" height="16" rx="2" fill="none" stroke="#fff" stroke-width="1.6"/><path d="M4 10h16" stroke="#fff" stroke-width="1.6"/></svg>
      Platform &amp; Products</div>
    <div class="tab">
      <svg class="icon" viewBox="0 0 24 24"><circle cx="12" cy="12" r="8" fill="none" stroke="#fff" stroke-width="1.6"/><circle cx="12" cy="12" r="3" fill="#fff"/></svg>
      Business Intelligence as a Service</div>
  </div>
  <div class="why-card" role="img" aria-label="Glowing network of connected data points">
    <h3>Community</h3>
    <p>KORVEL isn't just a platform—it's a movement. Join a growing community of healthcare leaders, housing professionals, data scientists, and innovators who are reshaping the future using data.</p>
    <span class="btn btn-fill">Read more</span>
  </div>

  <div class="center-head products-head">
    <span class="tag tag-light">Products Overview</span>
    <h2>KORVEL's product suite is designed to make critical data accessible, insightful, and actionable.</h2>
  </div>
  <div class="product-cards">
    <article class="product-card">
      <div class="art" role="img" aria-label="Teal network of people icons" style="background:linear-gradient(160deg,#04201f,#0f6b63 60%,#03110f)"></div>
      <h3>Public Data Access</h3>
      <p>Access curated, up-to-date public datasets that matter to your sector—ready to explore, compare, and layer into your own analysis.</p>
      <div class="more">Learn More ›</div>
    </article>
    <article class="product-card">
      <div class="art" role="img" aria-label="Rising green data chart" style="background:linear-gradient(160deg,#071a10,#2f8a4a 55%,#06140c)"></div>
      <h3>Climate Risk Scan</h3>
      <p>Identify, assess, and act on environmental and climate-related risks across your assets and communities.</p>
      <div class="more">Learn More ›</div>
    </article>
    <article class="product-card">
      <div class="art" role="img" aria-label="Blue financial graph overlay" style="background:linear-gradient(160deg,#061633,#2a64b0 55%,#051027)"></div>
      <h3>Pricing benchmark</h3>
      <p>Understand your true cost drivers and model future scenarios to plan with precision.</p>
      <div class="more">Learn More ›</div>
    </article>
  </div>
</section>

<section class="section audience">
  <span class="tag">Who is KORVEL For?</span>
  <h2>Data Without Limits. Insights Without Barriers.</h2>
  <p>KORVEL is built for professionals across the healthcare and social housing sectors who need smarter, faster, and more strategic ways to harness their data.</p>
  <span class="btn btn-fill">Read more</span>
  <div class="audience-card" role="img" aria-label="Team meeting around a table with laptops">
    <span class="tag">Key audiences</span>
    <h3>Sales &amp; Business Development Managers</h3>
    <p>Stay ahead of the curve with access to pricing benchmarks, sector demand forecasts, and real-time market insights. Spot new opportunities.</p>
    <span class="btn btn-fill">Read more</span>
  </div>
</section>

<section class="section testimonial">
  <span class="tag">Testimonial</span>
  <h2>Trusted by professionals across healthcare and social housing</h2>
  <div class="quote-card">
    <div class="person">
      <div class="avatar" role="img" aria-label="Portrait photo"></div>
      <div><strong>Marten Velde</strong><span>Director of Assets, Northfield Housing Trust</span></div>
    </div>
    <blockquote>With KORVEL's climate risk scan and asset data tools, we're finally able to prioritize maintenance based on both need and sustainability. It's a game-changer for long-term planning</blockquote>
    <div class="pager"><span>←</span><span>01 — 03</span><span>→</span></div>
    <span class="btn">case study</span>
  </div>
</section>

<div class="section partners">
  <span class="partner"></span><span class="partner"></span><span class="partner"></span><span class="partner"></span><span class="partner"></span><span class="partner"></span><span class="partner"></span><span class="partner"></span>
</div>

<section class="section action">
  <h2>See KORVEL in Action.</h2>
  <p>Discover how KORVEL can transform the way your team uses data. In just 30 minutes, we'll walk you through the platform, explore your specific needs.</p>
  <div class="buttons"><span class="btn btn-fill">Plan a demo</span><span class="btn">Start KORVEL</span></div>
</section>

<section class="section community" role="img" aria-label="Team hands stacked together in unity">
  <span class="tag">Community</span>
  <h2>More Than a Platform. A Movement.</h2>
  <p>KORVEL is more than just technology — it's a growing community of change-makers, analysts, sector leaders, and innovators using data to build a better future in healthcare and social housing.</p>
  <div class="buttons"><span class="btn btn-fill">Join the community</span><span class="btn btn-ghost-light">Learn More</span></div>
</section>

<section class="section contact">
  <h2>Ready to transform your business with KORVEL?</h2>
  <div class="form">
    <div class="row"><div class="field">Your Name*</div><div class="field">Your Phone*</div></div>
    <div class="row"><div class="field">Select Services*</div><div class="field">Your Email*</div></div>
    <div class="row"><div class="field">Message*</div></div>
    <span class="btn btn-fill">Submit</span>
  </div>
  <div class="contact-photo" role="img" aria-label="Glowing city skyline of data">Get in touch with us to learn more about how we can help your business achieve its goals.</div>
</section>

<footer class="section site-footer">
  <div class="footer-brand">KORVEL</div>
  <div class="socials"><span></span><span></span><span></span><span></span></div>
  <div class="col" style="left:440px"><h4>Quick Link</h4>What is KORVEL<br>Products<br>Who it's for<br>Community<br>About us<br>Contact us</div>
  <div class="col" style="left:680px"><h4>Service</h4>Residential<br>Commercial<br>House Maintenance<br>Electric Panel Repair</div>
  <div class="col" style="left:920px"><h4>Contact Us</h4>(555) 014-2290<br>hello@korvel.example<br>14 Harbor Lane, Springfield<br>Help &amp; Contact</div>
  <div class="bottom"><span>All Rights Reserved © 2025 KORVEL</span><span class="links"><span>Privacy Policy</span><span>Terms &amp; Condition</span><span>FAQ</span></span></div>
</footer>

</body>
</html>
```